Signage for Multi-family Veterans Housing community

Need a design concept package for the above. Need Historic feel design logo element together with "Alderwick Elders Commons"in serif font, for a Veterans (retired military) Affordable Housing community, in the Historic town of Larkmoor, California USA. I have attached an architectural drawing of the future housing community, that will need the signage. Also, attached are photos of the town of Windsor signage, for the historic downtown vibe, do not use the sign elements. Please include in the concept package a community ID sign similar to the craftsman community ID sign attached. The community ID sign will have the logo with name and address only, use a placeholder for Address. Thank you

Font styles to use
Serif
Sans Serif

Requirements
Should not have
• Please no American flags or other military references. Other than the word “I Veterans” in the title.

```html
<!DOCTYPE html>
<html lang="en">
<head>
<meta charset="utf-8">
<title>Alderwick Elders Commons – Community ID Sign</title>
<link href="https://fonts.googleapis.com/css2?family=Playfair+Display:wght@700;900&family=Montserrat:wght@500&display=swap" rel="stylesheet">
<style>
  :root {
    --sign-red: #990000;
    --sign-ink: #ffffff;
    --backdrop-dark: #363636;
    --backdrop-light: #8c8c8c;
    --ornament-tone: rgba(255, 255, 255, 0.85);
  }
  * { margin: 0; padding: 0; box-sizing: border-box; }
  html, body {
    width: 900px;
    height: 1200px;
    overflow: hidden;
  }
  body {
    background: linear-gradient(100deg, var(--backdrop-dark) 0%, var(--backdrop-light) 100%);
    position: relative;
  }
  .community-sign {
    position: absolute;
    left: 70px;
    top: 229px;
    width: 760px;
    height: 742px;
    filter: drop-shadow(0 14px 22px rgba(0, 0, 0, 0.35));
  }
  .sign-panel {
    position: absolute;
    inset: 0;
    width: 760px;
    height: 742px;
  }
  .sign-content {
    position: absolute;
    inset: 0;
    text-align: center;
    color: var(--sign-ink);
  }
  .ornament {
    position: absolute;
    left: 50%;
    transform: translateX(-50%);
    background: var(--ornament-tone);
    border-radius: 20px;
  }
  .ornament--crest { top: 84px; width: 186px; height: 50px; }
  .ornament--laurel { top: 362px; width: 330px; height: 40px; }
  .ornament--divider { top: 558px; width: 194px; height: 14px; border-radius: 7px; }
  .community-name {
    position: absolute;
    top: 158px;
    left: 0;
    right: 0;
    font-family: "Playfair Display", Georgia, serif;
    font-weight: 900;
    font-size: 100px;
    letter-spacing: 0.07em;
    line-height: 1;
  }
  .community-subname {
    position: absolute;
    top: 276px;
    left: 0;
    right: 0;
    font-family: "Playfair Display", Georgia, serif;
    font-weight: 700;
    font-size: 56px;
    line-height: 1;
    text-transform: uppercase;
  }
  .audience-band {
    position: absolute;
    top: 432px;
    left: 90px;
    width: 580px;
    height: 42px;
    background: var(--sign-ink);
    color: var(--sign-red);
    font-family: "Montserrat", Arial, sans-serif;
    font-weight: 500;
    font-size: 25px;
    line-height: 42px;
    text-transform: uppercase;
  }
  .housing-type {
    position: absolute;
    top: 484px;
    left: 0;
    right: 0;
    font-family: "Playfair Display", Georgia, serif;
    font-weight: 700;
    font-size: 26px;
    letter-spacing: 0.01em;
  }
  .location {
    position: absolute;
    top: 604px;
    left: 0;
    right: 0;
    font-family: "Montserrat", Arial, sans-serif;
    font-weight: 500;
    font-size: 35px;
    line-height: 46px;
  }
</style>
</head>
<body>
  <div class="community-sign">
    <svg class="sign-panel" viewBox="0 0 760 742" aria-hidden="true">
      <path d="M0,100 Q380,-100 760,100 L760,742 L0,742 Z" fill="var(--sign-red)"/>
      <path d="M10,106 Q380,-82 750,106 L750,732 L10,732 Z" fill="none" stroke="var(--sign-ink)" stroke-width="2.5"/>
      <path d="M19,112 Q380,-66 741,112 L741,723 L19,723 Z" fill="none" stroke="var(--sign-ink)" stroke-width="2.5"/>
    </svg>
    <div class="sign-content">
      <div class="ornament ornament--crest" role="img" aria-label="Decorative scroll flourish"></div>
      <h1 class="community-name">Alderwick</h1>
      <h2 class="community-subname">Elders Commons</h2>
      <div class="ornament ornament--laurel" role="img" aria-label="Pair of laurel branches ornament"></div>
      <p class="audience-band">For a Veterans (Retired Military)</p>
      <p class="housing-type">Affordable Housing Community</p>
      <div class="ornament ornament--divider" role="img" aria-label="Decorative line divider"></div>
      <p class="location">Historic town of Larkmoor,<br>California USA</p>
    </div>
  </div>
</body>
</html>
```